Business Brochure / White Paper

This white paper is a marketing document to showcase ourselves to other businesses (private hospitals and other premium healthcare providers). The document should consist of bold and beautiful graphics. As an example of the sort of thing that we mean, we have attached the "velmora sky lineage records" white paper. It should consist of several A4 pages.
The content for the white paper is attached. Note that the content document is only a scaffold for the white paper and the exact layout does not need to be followed (especially text boxes which have just been placed roughly). You are free to use your artistic license to move content around in order to make the document as catchy as possible.
We have also included graphics that we have purchased licenses to and that we encourage to be used as you see fit. Note that in some places we have added a note after two asterisks (i.e. **) when we would like you to add specific images/graphics.
All of the relevant documents and graphics/images to be used to make the white paper can be found at the below link:
https://www.filquarry.net/sh/zhtwmekbb41paxl/BBDN5K3TB8FWLPNTq1tGmeOWRc?dl=0
Feel free to ask any questions.
Good Luck!
Hi,
Thank you for your submissions so far.
Please use our dropbox link for an updated and much more specific brief on what we require in terms of content, layout, and components:
Please note that we must make a decision within 3 days' time.
Please also note that we cannot select a designer unless designs for ALL PAGES of the white paper are submitted.
Thank you and good luck!

```html
<!DOCTYPE html>
<html lang="en">
<head>
<meta charset="utf-8">
<title>Helixora White Paper – Precision Medicine Spread</title>
<link href="https://fonts.googleapis.com/css2?family=Montserrat:wght@300;400;500;600;700&display=swap" rel="stylesheet">
<style>
  :root {
    --bg: #e4e4e4;
    --paper: #ffffff;
    --ink: #3b3b3b;
    --ink-soft: #6a6a6a;
    --green: #8cc63f;
    --green-mid: #4db070;
    --teal: #3aa9a0;
    --blue: #3d8fc8;
    --navy: #1f5fa0;
    --line: #9fd3cc;
    --chip: #eef1f2;
  }
  * { box-sizing: border-box; margin: 0; padding: 0; }
  html, body { width: 1200px; height: 900px; overflow: hidden; }
  body {
    background: var(--bg);
    font-family: "Montserrat", Arial, sans-serif;
    color: var(--ink);
    display: flex;
    align-items: center;
    justify-content: center;
  }
  .spread {
    display: flex;
    box-shadow: 0 14px 40px rgba(0,0,0,0.12);
  }
  .page {
    position: relative;
    width: 537px;
    height: 760px;
    background: var(--paper);
    padding: 64px 56px 56px;
  }
  .page--left { border-right: 1px solid #ececec; }
  .section-title {
    font-size: 28px;
    font-weight: 500;
    color: var(--green);
    letter-spacing: 0.5px;
    margin-bottom: 18px;
  }
  .body-copy {
    font-size: 9.5px;
    line-height: 1.55;
    color: var(--ink-soft);
    margin-bottom: 10px;
  }
  .benefit-map { display: block; margin: 28px auto 0; }
  .benefit-label {
    font-family: "Montserrat", Arial, sans-serif;
    font-size: 10.5px;
    font-weight: 500;
    fill: var(--ink);
    text-anchor: middle;
  }
  .brand {
    position: absolute;
    right: 48px;
    bottom: 40px;
    display: flex;
    align-items: center;
    gap: 6px;
    font-size: 13px;
    font-weight: 600;
    color: var(--teal);
  }
  .brand__dot {
    width: 10px; height: 10px; border-radius: 50%;
    background: var(--green);
  }
  .brand-card {
    width: 110px;
    height: 48px;
    background: var(--chip);
    box-shadow: 0 2px 6px rgba(0,0,0,0.12);
    display: flex;
    align-items: center;
    justify-content: center;
    gap: 6px;
    font-size: 13px;
    font-weight: 600;
    color: var(--teal);
    margin-bottom: 14px;
  }
  .service-title {
    font-size: 22px;
    font-weight: 400;
    color: var(--green);
    margin: 22px 0 10px;
  }
  .service-title:first-of-type { margin-top: 0; }
  .stats { display: flex; gap: 14px; margin-bottom: 12px; align-items: flex-end; }
  .stat { display: flex; align-items: baseline; gap: 6px; }
  .stat__value { font-size: 18px; font-weight: 500; color: var(--blue); }
  .stat__label { font-size: 8px; color: var(--ink-soft); }
  .stat-divider { width: 1px; height: 22px; background: #cfcfcf; }
</style>
</head>
<body>
  <main class="spread">
    <section class="page page--left">
      <h1 class="section-title">PRECISION MEDICINE</h1>
      <p class="body-copy">Leading medical centres across the world now rely on genomic insight to guide treatment. Precision medicine uses an individual's genetic profile to shape prevention, diagnosis and therapy, moving care away from a one-size-fits-all model toward decisions built on each patient's biology, history and environment for better results.</p>
      <p class="body-copy">Since the first human genome was decoded, the cost of sequencing has fallen sharply while speed has grown. Hospitals can now offer genomic testing as part of routine care, giving clinicians clear data to select medicines, adjust doses and spot inherited risks long before symptoms appear.</p>
      <p class="body-copy">Helixora partners with private hospitals and premium providers to bring sequencing, analysis and reporting into one secure service, ready for clinical use today.</p>

      <svg class="benefit-map" width="420" height="380" viewBox="0 0 420 380" aria-label="Benefits of precision medicine">
        <g stroke="var(--line)" stroke-width="1.2">
          <line x1="200" y1="190" x2="175" y2="85"/>
          <line x1="200" y1="190" x2="295" y2="120"/>
          <line x1="200" y1="190" x2="320" y2="210"/>
          <line x1="200" y1="190" x2="190" y2="310"/>
          <line x1="200" y1="190" x2="75" y2="215"/>
        </g>
        <circle cx="200" cy="190" r="11" fill="var(--teal)"/>
        <circle cx="175" cy="85" r="10" fill="var(--teal)"/>
        <circle cx="295" cy="120" r="10" fill="var(--green)"/>
        <circle cx="320" cy="210" r="10" fill="var(--green-mid)"/>
        <circle cx="190" cy="310" r="10" fill="var(--blue)"/>
        <circle cx="75" cy="215" r="10" fill="var(--navy)"/>
        <text class="benefit-label" x="175" y="45">INCREASE THERAPY</text>
        <text class="benefit-label" x="175" y="59">EFFECTIVENESS</text>
        <text class="benefit-label" x="300" y="82">IMPROVE MEDICAL</text>
        <text class="benefit-label" x="300" y="96">COMPLIANCE</text>
        <text class="benefit-label" x="340" y="168">IMPROVE ECONOMIC</text>
        <text class="benefit-label" x="340" y="182">EFFICIENCY</text>
        <text class="benefit-label" x="95" y="168">IMPROVE PATIENT</text>
        <text class="benefit-label" x="95" y="182">CARE</text>
        <text class="benefit-label" x="120" y="290">LIMIT ADVERSE</text>
        <text class="benefit-label" x="120" y="304">OUTCOMES</text>
      </svg>

      <div class="brand"><span class="brand__dot"></span>helixora</div>
    </section>

    <section class="page page--right">
      <div class="brand-card"><span class="brand__dot"></span>helixora</div>

      <h2 class="service-title">Whole Genome Sequencing</h2>
      <div class="stats">
        <div class="stat"><span class="stat__value">13</span><span class="stat__label">years to sequence</span></div>
        <span class="stat-divider"></span>
        <div class="stat"><span class="stat__value">2.7</span><span class="stat__label">billion to complete</span></div>
      </div>
      <p class="body-copy">The first human genome took thirteen years and billions to complete. Today whole genome sequencing reads all three billion bases of DNA in days, revealing variants across coding and non-coding regions to support diagnosis, research and lifelong care planning.</p>

      <h2 class="service-title">Whole Exome Sequencing</h2>
      <p class="body-copy">Whole exome sequencing focuses on the protein-coding regions of the genome, where most known disease-causing variants are found. It offers a faster, lower-cost route to answers for patients with complex or undiagnosed conditions.</p>

      <h2 class="service-title">Disease Risk Genotyping</h2>
      <p class="body-copy">Disease risk genotyping screens for known markers linked to common conditions such as heart disease, diabetes and certain cancers, helping clinicians plan early checks and targeted prevention.</p>

      <div class="brand"><span class="brand__dot"></span>helixora</div>
    </section>
  </main>
</body>
</html>
```